Stationary for 2-office law firm with global theme

I need stationary with contact info for two offices. I'd like the same letterhead design to work for printing on stationary and also for digital use in Word. The colors and feel should match the new logo, which is a stylized globe with and "F" in it. I'd also like envelopes with an eye-catching design.

Target Market(s)

U.S. citizens seeking dual citizenship with Italy or Ireland

Industry/Entity Type

Law

Font styles to use
Serif
Sans Serif
Other font styles liked:
• To match the logo?

Colors
0054AA
0677BA
7BADD7
CADEEF
E8F1F8

Requirements
Must have
• Clean, modern design incorporating new logo

```html
<!DOCTYPE html>
<html lang="en">
<head>
<meta charset="utf-8">
<title>Valmont Law — Stationery</title>
<link rel="stylesheet" href="https://fonts.googleapis.com/css2?family=Roboto:wght@400;500;700&family=Montserrat:wght@400;500;700&family=Great+Vibes&display=swap">
<style>
  :root {
    --navy: #003a70;
    --sky: #00b9f2;
    --ink: #2d2d2d;
    --paper: #ffffff;
    --paper-soft: #f7f8f9;
    --backdrop: #d2d3d4;
    --mark-tint: #e6f6fc;
    --mark-grey: #e9eef2;
  }
  * { box-sizing: border-box; margin: 0; padding: 0; }
  html, body { width: 1200px; height: 923px; overflow: hidden; }
  body { background: var(--backdrop); font-family: "Roboto", sans-serif; color: var(--ink); position: relative; }

  .sheet { position: absolute; background: var(--paper); overflow: hidden; }

  /* Letterhead */
  .letterhead { left: 92px; top: 130px; width: 474px; height: 669px; }
  .top-bar { position: absolute; top: 0; height: 7px; }
  .top-bar--navy-a { left: 0; width: 317px; background: var(--navy); }
  .top-bar--sky { left: 320px; width: 122px; background: var(--sky); }
  .top-bar--navy-b { left: 445px; width: 29px; background: var(--navy); }

  .brand { position: absolute; display: flex; flex-direction: column; align-items: center; }
  .brand__dot { border-radius: 50%; background: var(--sky); }
  .brand__name { font-family: "Montserrat", sans-serif; font-weight: 700; color: var(--navy); white-space: nowrap; letter-spacing: 0.02em; }

  .letterhead .brand { left: 34px; top: 50px; width: 130px; }
  .letterhead .brand__dot { width: 40px; height: 40px; margin-bottom: 10px; }
  .letterhead .brand__name { font-size: 17px; }

  .contact { position: absolute; list-style: none; font-family: "Montserrat", sans-serif; font-size: 6.4px; font-variant: small-caps; letter-spacing: 0.09em; color: #555; }
  .contact li { display: flex; align-items: flex-start; gap: 5px; line-height: 9.6px; }
  .contact li + li { margin-top: 0.5px; }
  .contact li.gap { margin-top: 4px; }
  .contact svg { width: 6px; height: 7px; flex: none; margin-top: 1px; fill: var(--sky); }
  .letterhead .contact { left: 335px; top: 46px; }

  .recipient { position: absolute; left: 42px; top: 182px; }
  .recipient__to, .recipient__name { font-size: 9.6px; font-weight: 500; color: #222; line-height: 15.5px; }
  .recipient__role { font-size: 8.2px; line-height: 12px; }
  .date { position: absolute; right: 35px; top: 230px; font-size: 8.2px; }
  .date strong { font-size: 9.6px; font-weight: 500; }

  .decor { position: absolute; }
  .letterhead .decor { left: 120px; top: 370px; width: 354px; height: 299px;
    background: radial-gradient(ellipse at 75% 75%, var(--mark-grey) 0%, var(--mark-tint) 45%, rgba(255,255,255,0) 72%); }

  .body-copy { position: absolute; left: 42px; top: 261px; width: 397px; font-size: 8.2px; line-height: 16.7px; text-align: justify; }
  .body-copy p + p { margin-top: 16.5px; }

  .signoff { position: absolute; left: 42px; top: 516px; }
  .signoff__script { font-family: "Great Vibes", cursive; font-size: 20px; color: #333; line-height: 22px; }
  .signoff__name { font-family: "Montserrat", sans-serif; font-weight: 700; font-size: 11.5px; letter-spacing: 0.06em; color: var(--navy); margin-top: 2px; }
  .signoff__role { font-family: "Montserrat", sans-serif; font-size: 5.8px; letter-spacing: 0.08em; color: var(--sky); }

  /* Envelopes */
  .envelope { width: 446px; height: 222px; background: var(--paper-soft); }
  .envelope--back { left: 664px; top: 216px; }
  .envelope--front { left: 608px; top: 324px; }
  .flap { position: absolute; left: 0; top: 0; width: 446px; height: 75px; display: flex; align-items: center; justify-content: center; }
  .envelope--back .flap { background: var(--navy); clip-path: polygon(0 0, 100% 0, 95% 100%, 5% 100%); }
  .envelope--front .flap { background: var(--sky); clip-path: polygon(0 0, 100% 0, 95% 100%, 5% 100%); }
  .flap .brand { position: static; flex-direction: row; gap: 7px; }
  .flap .brand__dot { width: 27px; height: 27px; }
  .flap .brand__name { font-size: 13px; }
  .envelope--back .brand__name { color: var(--sky); }
  .envelope--front .brand__dot { background: var(--navy); }

  /* Window envelope */
  .dl { left: 608px; top: 577px; width: 446px; height: 223px; background: var(--paper-soft); }
  .side-bar { position: absolute; left: 0; width: 7px; }
  .side-bar--a { top: 0; height: 151px; background: var(--navy); }
  .side-bar--b { top: 155px; height: 36px; background: var(--sky); }
  .side-bar--c { top: 194px; height: 29px; background: var(--navy); }
  .dl .brand { left: 25px; top: 30px; width: 115px; }
  .dl .brand__dot { width: 38px; height: 38px; margin-bottom: 10px; }
  .dl .brand__name { font-size: 14.5px; }
  .dl .contact { left: 34px; top: 159px; }
  .dl .decor { left: 250px; top: 20px; width: 196px; height: 203px;
    background: radial-gradient(ellipse at 70% 70%, var(--mark-grey) 0%, var(--mark-tint) 48%, rgba(247,248,249,0) 75%); }
</style>
</head>
<body>

<svg width="0" height="0" style="position:absolute" aria-hidden="true">
  <symbol id="icon-pin" viewBox="0 0 10 12"><path d="M5 0a4 4 0 0 0-4 4c0 3 4 8 4 8s4-5 4-8a4 4 0 0 0-4-4zm0 5.6A1.6 1.6 0 1 1 5 2.4a1.6 1.6 0 0 1 0 3.2z"/></symbol>
  <symbol id="icon-phone" viewBox="0 0 10 12"><path d="M2.2 1.5l1.6-.4 1 2.4-1 .8a6 6 0 0 0 2.6 3.1l.9-.9 2.3 1.2-.5 1.6C6.5 10 1.4 5.6 2.2 1.5z"/></symbol>
  <symbol id="icon-mobile" viewBox="0 0 10 12"><path d="M2.5 0h5a1 1 0 0 1 1 1v10a1 1 0 0 1-1 1h-5a1 1 0 0 1-1-1V1a1 1 0 0 1 1-1zm.5 1.5v7.5h4V1.5z"/></symbol>
  <symbol id="icon-mail" viewBox="0 0 10 12"><path d="M0 3h10v6H0zm1 .8L5 6.6l4-2.8z" fill-rule="evenodd"/></symbol>
  <symbol id="icon-web" viewBox="0 0 10 12"><path d="M5 1.5a4.5 4.5 0 1 0 0 9 4.5 4.5 0 0 0 0-9zm0 1.2a3.3 3.3 0 0 1 0 6.6 3.3 3.3 0 0 1 0-6.6zM4.3 3v6h1.4V3z"/></symbol>
</svg>

<section class="sheet letterhead" aria-label="Letterhead">
  <div class="top-bar top-bar--navy-a"></div>
  <div class="top-bar top-bar--sky"></div>
  <div class="top-bar top-bar--navy-b"></div>

  <div class="decor" role="img" aria-label="Faint brand mark decoration"></div>

  <div class="brand">
    <span class="brand__dot"></span>
    <span class="brand__name">VALMONT LAW</span>
  </div>

  <ul class="contact">
    <li><svg><use href="#icon-pin"/></svg><span>4750 Harlow Avenue<br>Carver, CT 06812</span></li>
    <li class="gap"><svg><use href="#icon-pin"/></svg><span>4750 Harlow Avenue<br>Carver, CT 06812</span></li>
    <li class="gap"><svg><use href="#icon-phone"/></svg><span>(555) 214-0387</span></li>
    <li><svg><use href="#icon-mobile"/></svg><span>(555) 214-0387</span></li>
    <li><svg><use href="#icon-mail"/></svg><span>MARA@VALMONTLAW.COM</span></li>
    <li><svg><use href="#icon-web"/></svg><span>VALMONTLAW.COM</span></li>
  </ul>

  <div class="recipient">
    <p class="recipient__to">To</p>
    <p class="recipient__name">Name Here</p>
    <p class="recipient__role">Position</p>
  </div>
  <p class="date"><strong>Date:</strong> DD / MM / YY</p>

  <div class="body-copy">
    <p>Lorem Ipsum is simply dummy text of the printing and typesetting industry. Lorem Ipsum has been the industry's standard dummy text ever since the 1500s, when an unknown printer took a galley of type and scrambled it to make a type specimen book.simply dummy text of the printing .</p>
    <p>Simply dummy text of the printing and typesetting industry. Lorem Ipsum has been the industry's standard dummy text ever since the 1500s, when an unknown printer took a galley of type and scrambled it to make a type specimen book. It has survived not only five centuries, but also the leap into electronic typesetting, remaining essentially unchanged. It was popularised .</p>
    <p>When an unknown printer took a galley of type and scrambled it to make a type specimen book. It has survived not only five centuries, but also the leap into electronic. Lorem Ipsum dummy text. standard dummy text ever since the 1500s, when an unknown printer took a galley of type and scrambled it to make a type specimen book.</p>
  </div>

  <div class="signoff">
    <p class="signoff__script">Sign Here</p>
    <p class="signoff__name">MARA ELLISON</p>
    <p class="signoff__role">LAWYER</p>
  </div>
</section>

<section class="sheet envelope envelope--back" aria-label="Envelope with navy flap">
  <div class="flap">
    <div class="brand"><span class="brand__dot"></span><span class="brand__name">VALMONT LAW</span></div>
  </div>
</section>

<section class="sheet envelope envelope--front" aria-label="Envelope with sky blue flap">
  <div class="flap">
    <div class="brand"><span class="brand__dot"></span><span class="brand__name">VALMONT LAW</span></div>
  </div>
</section>

<section class="sheet dl" aria-label="Envelope front">
  <div class="side-bar side-bar--a"></div>
  <div class="side-bar side-bar--b"></div>
  <div class="side-bar side-bar--c"></div>
  <div class="decor" role="img" aria-label="Faint brand mark decoration"></div>
  <div class="brand">
    <span class="brand__dot"></span>
    <span class="brand__name">VALMONT LAW</span>
  </div>
  <ul class="contact">
    <li><svg><use href="#icon-pin"/></svg><span>4750 Harlow Avenue<br>Carver, CT 06812</span></li>
    <li class="gap"><svg><use href="#icon-pin"/></svg><span>4750 Harlow Avenue<br>Carver, CT 06812</span></li>
  </ul>
</section>

</body>
</html>
```